Premium Personal Brand — Facebook Banner (Used Across All Platforms)

Update — Additional Color Direction
In addition to the dark charcoal/slate direction already described, I'm also interested in seeing variants with:
Dark navy blue — Deep, authoritative, intelligence-community feel. Same textured/matte treatment, not flat or bright.
Warm charcoal with steel blue accent — Keep the dark base but introduce a subtle steel blue gradient, accent line, or tonal shift. Sophisticated, modern, adds dimension without adding color noise.
Both should maintain the same premium, restrained, architectural feel described in the original brief. No bright blues, no corporate PowerPoint energy — think midnight, think depth, think weight.
Everything else in the brief remains the same.
I am building a premium personal brand as an executive advisor to founders ($5M+ revenue).
This contest is Facebook-banner–focused, but the design must represent a visual system that will be reused across:
- LinkedIn
- YouTube
I- nstagram
- X (Twitter)
- Website hero sections and other brand touchpoints
Think of the Facebook banner as the primary expression of the brand — not a one-off graphic.
This project is about discovering a high-end visual style and brand feel, not decoration.
What to design
Please submit one cohesive visual system, shown primarily as:
- Facebook banner (primary focus)
The same design language should clearly translate to all platforms listed above.
Designers are responsible for using the current recommended dimensions for each platform.
Quick clarification on background direction:
Backgrounds should have depth and texture, not flat color fields. Avoid pure white, light grey, or solid black backgrounds. Think matte, architectural materials — stone, graphite, concrete, steel — not blank canvases. Subtle tonal variation is encouraged. Obvious gradients or decorative patterns are not.
Text to use
Primary Headline:
- Your Business Is Too Valuable To Be Run On Hope.
Subheadline:
- You didn’t build a business to become its prisoner.
Name:
Paul Whitaker
The headline should be the dominant visual element.
Logo note (important)
My personal logo is currently being finalized.
For this contest:
- Use a simple “PW” monogram placeholder
- Clean, bold, geometric sans-serif
- Do not design a logo
- The winning design must allow an easy logo swap later.
Headshot note (important)
- Please do not include a headshot in the banner design.
- Most platforms display a circular profile image separately.
- The banner should stand on its own using typography, layout, and tone only.
- Design the banner assuming the profile photo will sit nearby, not inside the banner.
Style direction
The design should feel:
- Premium
- Calm
- Confident
- Restrained
- High-trust
- Dark, neutral backgrounds are preferred.
- Fewer elements are better than more.
Think:
- Owner-level advisor
- Private equity / boardroom tone
- Industrial, Modern, Minimalist, Elite, Architectural, not decorative
What to avoid
Please do not submit designs that feel:
- Promotional, hype-driven, or salesy
- Like a coach, guru, or agency
- Bright, colorful, or gradient-heavy
- Busy or over-designed
- Based on stock photos
- No motivational speaker energy.
Reaction test
- If someone sees this banner on Facebook (or later on LinkedIn, YouTube, etc.), the reaction should be:
“That person is serious. I’d trust them with important decisions.”
Final note
- I am not looking for many variations.
- I am looking for one strong visual direction you believe in.
Simple beats clever.
- Restraint beats decoration.

```html
<!DOCTYPE html>
<html lang="en">
<head>
<meta charset="utf-8">
<title>Paul Whitaker — Banner</title>
<link rel="stylesheet" href="https://fonts.googleapis.com/css2?family=Montserrat:wght@300;800&family=Work+Sans:wght@400&display=swap">
<style>
  :root {
    --page: #efefeb;
    --charcoal-deep: #121715;
    --charcoal: #1b221f;
    --slate-light: #3a4248;
    --ink: #ffffff;
    --accent: #8fe31c;
  }
  * { margin: 0; padding: 0; box-sizing: border-box; }
  html, body {
    width: 1200px;
    height: 1000px;
    overflow: hidden;
    background: var(--page);
  }
  .banner {
    position: absolute;
    left: 0;
    top: 236px;
    width: 1200px;
    height: 527px;
    overflow: hidden;
    background: var(--charcoal-deep);
  }
  .banner__backdrop {
    position: absolute;
    inset: 0;
    background:
      radial-gradient(ellipse 360px 420px at 850px 260px, rgba(58, 66, 72, 0.55), transparent 80%),
      linear-gradient(90deg, var(--charcoal) 0%, var(--charcoal-deep) 100%);
  }
  .banner__copy {
    position: absolute;
    left: 166px;
    top: 150px;
    color: var(--ink);
  }
  .headline {
    font-family: "Montserrat", sans-serif;
    font-weight: 300;
    font-size: 43px;
    line-height: 43px;
    letter-spacing: 0.045em;
    white-space: nowrap;
  }
  .headline strong { font-weight: 800; }
  .subheadline {
    margin-top: 12px;
    font-family: "Work Sans", sans-serif;
    font-weight: 400;
    font-size: 23px;
    line-height: 25px;
    letter-spacing: 0.02em;
    white-space: nowrap;
  }
  .monogram {
    position: absolute;
    left: 842px;
    top: 263px;
    transform: translate(-50%, -50%);
    font-family: "Montserrat", sans-serif;
    font-weight: 300;
    font-size: 92px;
    line-height: 1;
    letter-spacing: -0.02em;
    color: var(--accent);
  }
</style>
</head>
<body>
  <section class="banner">
    <div class="banner__backdrop" role="img" aria-label="Photograph of a dark concrete room lit by a single overhead spotlight"></div>
    <div class="banner__copy">
      <h1 class="headline">Your <strong>Business Is Too</strong><br><strong>Valuable</strong> To Be Run<br>On <strong>Hope</strong></h1>
      <p class="subheadline">You didn't build a<br>business to become<br>its prisoner</p>
    </div>
    <div class="monogram">PW</div>
  </section>
</body>
</html>
```